Cobre Ridge Grill Rub bottle label design

I need a design for 2 different seasoning bottles
looking for something classy and clean.
One of the spices will be named TOPGRD. I would like to see a creative design for the name. I included the label dimensions as an attachment. I also included a picture of some spice bottles I saw only that I like. they dont have to be exactly like that but i like the matte black with the "foil" metallic colors on the bottom. I also want to include somewhere on the front of the bottle that I am a 3x world BBQ champion. I also included my logo on the attachments on the bottom. if you look at the label dimensions attachment there is an area for the nutrition fact and upc barcode. I have that info that i can give you and just plug it into the design. Also on the other side panel I have a brief description that will go on that side that I can provide you as well so you can plug it in.
Target Market(s)
Retail stores
Requirements
Must have
- My logo. I can provide to you.
Should say 3x BBQ world champion somewhere on front of the bottle
Name of the Seasoning TOPGRD and Dorado. 2 different
A brief description/story that will go on the side panel. I will send that to you.
Should have Texas incorporated into the design not so prominent.
Nice to have
- Figures or shapes of animals like a chicken, pig, cow. Small so that people can see what they can use that seasoning for.

```html
<!DOCTYPE html>
<html lang="en">
<head>
<meta charset="utf-8">
<title>Cobre Ridge Grill Rub – Seasoning Label Concept</title>
<link rel="stylesheet" href="https://fonts.googleapis.com/css2?family=Montserrat:wght@300;400;800&family=Oswald:wght@600&family=Roboto+Slab:wght@400;700&display=swap">
<style>
:root{
  --ink:#111111;
  --matte:#1c1c1c;
  --label:#181818;
  --red:#c0263a;
  --navy:#1f3566;
  --silver:#c9c9c9;
  --silver-dark:#8a8a8a;
  --white:#ffffff;
  --paper:#ffffff;
  --rule:#333333;
}
*{box-sizing:border-box;margin:0;padding:0}
html,body{width:1200px;height:1000px;overflow:hidden;background:var(--paper)}
.board{position:relative;width:1200px;height:1000px;font-family:"Montserrat",sans-serif;color:var(--ink)}

/* left column */
.divider{position:absolute;left:330px;top:70px;width:1px;height:855px;background:var(--rule)}
.brand-mark{position:absolute;left:40px;top:140px;width:250px;text-align:center;font-family:"Roboto Slab",serif;font-weight:700;font-size:22px;line-height:1.25;color:var(--navy)}
.brand-mark .dot{display:inline-block;width:14px;height:14px;background:var(--red);border-radius:50%;margin-bottom:8px}
.concept{position:absolute;left:0;top:405px;width:330px;text-align:center}
.concept-title{font-weight:800;font-size:17px;letter-spacing:.5px}
.concept-list{margin-top:42px;list-style:none;font-weight:300;font-size:20px;letter-spacing:6px}
.concept-list li{height:34px}
.concept-list .plus{font-weight:800;font-size:32px;letter-spacing:0;line-height:30px}
.palette{position:absolute;left:0;top:0}

/* front labels */
.front{position:absolute;top:228px;width:198px;height:338px;background:var(--label);overflow:hidden}
.front--topgrd{left:502px;--accent:var(--red)}
.front--dorado{left:800px;--accent:var(--navy)}
.tab{position:absolute;left:61px;top:8px;width:76px;height:64px;background:var(--accent);border-radius:0 0 4px 4px;display:flex;flex-direction:column;align-items:center;justify-content:center;gap:3px}
.tab-name{font-family:"Roboto Slab",serif;font-weight:700;font-size:7px;line-height:1.15;color:var(--white);text-align:center;text-transform:uppercase}
.tab .dot{width:7px;height:7px;border-radius:50%;background:var(--white)}
.state-shape{position:absolute;left:44px;top:104px;width:112px;height:112px;background:var(--accent);opacity:.5}
.animal-art{position:absolute;left:66px;top:100px;width:72px;height:34px;border-radius:18px 18px 6px 6px;background:linear-gradient(180deg,#d8d8d8,#9a9a9a)}
.product-name{position:absolute;left:0;width:100%;top:140px;text-align:center;font-family:"Oswald",sans-serif;font-weight:600;font-size:50px;letter-spacing:1px;color:#ececec;text-shadow:2px 2px 0 #000}
.product-sub{position:absolute;left:14px;right:14px;top:214px;display:flex;align-items:center;gap:6px;font-family:"Roboto Slab",serif;font-weight:700;font-size:11px;color:var(--accent);white-space:nowrap}
.product-sub::before,.product-sub::after{content:"";flex:1;height:1px;background:var(--accent)}
.champ{position:absolute;left:136px;top:256px;width:52px;height:52px;border-radius:50%;background:var(--accent);border:4px solid var(--silver);display:flex;align-items:center;justify-content:center;font-family:"Roboto Slab",serif;font-style:italic;font-size:20px;color:var(--white)}
.champ-note{position:absolute;left:126px;top:311px;width:70px;text-align:center;font-size:5px;font-weight:800;color:var(--silver);letter-spacing:.3px}
.volume{position:absolute;left:0;width:100%;top:318px;text-align:center;font-family:"Roboto Slab",serif;font-size:9px;color:#ddd}

/* callouts */
.callout{position:absolute;font-weight:400;font-size:15px;letter-spacing:4px;line-height:21px;color:#333}
.callout--matte{left:1050px;top:228px}
.callout--foil{left:1025px;top:627px}
.arrows{position:absolute;left:0;top:0}

/* flat full labels */
.flat{position:absolute;top:730px;width:384px;height:195px;background:var(--label);border-radius:10px;overflow:hidden}
.flat--topgrd{left:370px;--accent:var(--red)}
.flat--dorado{left:772px;--accent:var(--navy)}
.flat .tab{left:178px;top:0;width:30px;height:46px}
.flat .tab-name{font-size:3.5px}
.flat .tab .dot{width:4px;height:4px}
.story{position:absolute;left:14px;top:32px;width:118px;font-family:"Roboto Slab",serif;font-weight:700;font-size:6.2px;line-height:1.45;color:#e6e6e6}
.story::before{content:"\201C";position:absolute;left:-2px;top:-6px;font-size:22px;color:#e6e6e6;font-family:Georgia,serif}
.story p{padding-left:14px}
.flat .state-shape{left:156px;top:52px;width:60px;height:60px}
.flat .animal-art{left:168px;top:52px;width:40px;height:18px}
.flat .product-name{top:72px;font-size:27px;left:90px;width:206px}
.flat .product-sub{left:148px;right:148px;top:112px;font-size:6px;gap:3px}
.flat .champ{left:213px;top:120px;width:28px;height:28px;font-size:11px;border-width:2px}
.flat .volume{top:178px;font-size:6px;left:90px;width:206px}
.nutrition{position:absolute;right:16px;top:13px;width:86px;background:var(--white);padding:3px 3px 4px;font-family:Arial,sans-serif;color:#000;font-size:4.2px;line-height:1.35}
.nutrition h3{font-size:8.5px;font-weight:800;border-bottom:.5px solid #000;line-height:1.1}
.nutrition .row{display:flex;justify-content:space-between;border-bottom:.4px solid #000}
.nutrition .thick{border-bottom:2.5px solid #000}
.nutrition .cal{font-size:8px;font-weight:800;display:flex;justify-content:space-between;border-bottom:1.5px solid #000}
.nutrition .in{padding-left:4px}
.nutrition .foot{margin-top:2px;font-size:3.4px;line-height:1.3}
</style>
</head>
<body>
<main class="board">

  <div class="brand-mark"><span class="dot"></span><br>Cobre Ridge<br>Grill Rub</div>

  <section class="concept">
    <h2 class="concept-title">CONCEPT:</h2>
    <ul class="concept-list">
      <li>PREMIUM</li>
      <li class="plus">+</li>
      <li>TEXAN</li>
      <li class="plus">+</li>
      <li>DELICIOUS</li>
    </ul>
  </section>

  <svg class="palette" width="330" height="1000" aria-label="Colour palette">
    <defs>
      <linearGradient id="foil" x1="0" y1="0" x2="1" y2="1">
        <stop offset="0" stop-color="#8a8a8a"/><stop offset=".45" stop-color="#f4f4f4"/><stop offset="1" stop-color="#7a7a7a"/>
      </linearGradient>
    </defs>
    <circle cx="101" cy="748" r="43" fill="#fff" stroke="#111" stroke-width="1"/>
    <circle cx="182" cy="760" r="25" fill="#c0263a"/>
    <circle cx="246" cy="733" r="22" fill="url(#foil)"/>
    <circle cx="136" cy="815" r="25" fill="#1f3566"/>
    <circle cx="240" cy="832" r="57" fill="#000"/>
  </svg>

  <div class="divider"></div>

  <!-- front labels -->
  <article class="front front--topgrd">
    <div class="tab"><span class="dot"></span><span class="tab-name">Cobre Ridge<br>Grill Rub</span></div>
    <div class="state-shape" role="img" aria-label="Faint Texas state silhouette in red"></div>
    <div class="animal-art" role="img" aria-label="Small illustration of a cow, pig and chicken"></div>
    <h1 class="product-name">TOPGRD</h1>
    <p class="product-sub">MEAT SEASONING</p>
    <div class="champ">3x</div>
    <p class="champ-note">WORLD BBQ CHAMPION</p>
    <p class="volume">250ml</p>
  </article>

  <article class="front front--dorado">
    <div class="tab"><span class="dot"></span><span class="tab-name">Cobre Ridge<br>Grill Rub</span></div>
    <div class="state-shape" role="img" aria-label="Faint Texas state silhouette in navy"></div>
    <div class="animal-art" role="img" aria-label="Small illustration of a cow, pig and chicken"></div>
    <h1 class="product-name">DORADO</h1>
    <p class="product-sub">MEAT SEASONING</p>
    <div class="champ">3x</div>
    <p class="champ-note">WORLD BBQ CHAMPION</p>
    <p class="volume">250ml</p>
  </article>

  <p class="callout callout--matte">MATTE<br>BLACK</p>
  <p class="callout callout--foil">SILVER<br>FOIL</p>
  <svg class="arrows" width="1200" height="1000" aria-hidden="true">
    <path d="M1100 280 Q1085 318 1018 332" fill="none" stroke="#555" stroke-width="1"/>
    <path d="M1018 332 l8 -6 M1018 332 l9 3" fill="none" stroke="#555" stroke-width="1"/>
    <path d="M1010 540 Q1060 560 1048 615" fill="none" stroke="#555" stroke-width="1"/>
    <path d="M1048 615 l-5 -8 M1048 615 l5 -7" fill="none" stroke="#555" stroke-width="1"/>
  </svg>

  <!-- full wrap labels -->
  <article class="flat flat--topgrd">
    <div class="story"><p>Built over years of smoke, fire and long nights at the pit, this blend brings bold pepper, garlic and chili heat to every cut. It was crafted for brisket, ribs and wings alike. Shake it on generously, let it rest, and cook low and slow for a crust worth bragging about.</p></div>
    <div class="tab"><span class="dot"></span><span class="tab-name">Cobre Ridge<br>Grill Rub</span></div>
    <div class="state-shape" role="img" aria-label="Faint Texas state silhouette in red"></div>
    <div class="animal-art" role="img" aria-label="Small illustration of a cow, pig and chicken"></div>
    <h2 class="product-name">TOPGRD</h2>
    <p class="product-sub">MEAT SEASONING</p>
    <div class="champ">3x</div>
    <p class="volume">250ml</p>
    <div class="nutrition">
      <h3>Nutrition Facts</h3>
      <div class="row"><span>1 serving per container</span></div>
      <div class="row thick"><b>Serving size</b><b>1/4 cup (40g)</b></div>
      <div class="cal"><span>Calories</span><span>120</span></div>
      <div class="row"><span></span><b>% Daily Value*</b></div>
      <div class="row"><b>Total Fat 0g</b><span>0%</span></div>
      <div class="row in"><span>Saturated Fat 0g</span><span>0%</span></div>
      <div class="row in"><span>Trans Fat 0g</span><span></span></div>
      <div class="row"><b>Cholesterol 0mg</b><span>0%</span></div>
      <div class="row"><b>Sodium 10mg</b><span>0%</span></div>
      <div class="row"><b>Total Carbohydrate 32g</b><span>12%</span></div>
      <div class="row in"><span>Dietary Fiber 2g</span><span>7%</span></div>
      <div class="row in"><span>Total Sugars 28g</span><span></span></div>
      <div class="row thick"><b>Protein 1g</b><span></span></div>
      <div class="row"><span>Vitamin D 0mcg</span><span>0%</span></div>
      <div class="row"><span>Calcium 20mg</span><span>2%</span></div>
      <div class="row"><span>Iron 0.7mg</span><span>4%</span></div>
      <div class="row"><span>Potassium 290mg</span><span>6%</span></div>
      <p class="foot">*The % Daily Value tells you how much a nutrient in a serving adds to a daily diet. Ingredients: salt, spices, garlic.</p>
    </div>
  </article>

  <article class="flat flat--dorado">
    <div class="story"><p>A bright, herb forward blend of parsley, onion, lemon and cracked pepper, made for chicken, pork and fish. Dorado keeps things clean and fresh while still carrying that Texas pit flavor. Rub it in before grilling or finish with a pinch right before you serve.</p></div>
    <div class="tab"><span class="dot"></span><span class="tab-name">Cobre Ridge<br>Grill Rub</span></div>
    <div class="state-shape" role="img" aria-label="Faint Texas state silhouette in navy"></div>
    <div class="animal-art" role="img" aria-label="Small illustration of a cow, pig and chicken"></div>
    <h2 class="product-name">DORADO</h2>
    <p class="product-sub">MEAT SEASONING</p>
    <div class="champ">3x</div>
    <p class="volume">250ml</p>
    <div class="nutrition">
      <h3>Nutrition Facts</h3>
      <div class="row"><span>1 serving per container</span></div>
      <div class="row thick"><b>Serving size</b><b>1/4 cup (40g)</b></div>
      <div class="cal"><span>Calories</span><span>120</span></div>
      <div class="row"><span></span><b>% Daily Value*</b></div>
      <div class="row"><b>Total Fat 0g</b><span>0%</span></div>
      <div class="row in"><span>Saturated Fat 0g</span><span>0%</span></div>
      <div class="row in"><span>Trans Fat 0g</span><span></span></div>
      <div class="row"><b>Cholesterol 0mg</b><span>0%</span></div>
      <div class="row"><b>Sodium 10mg</b><span>0%</span></div>
      <div class="row"><b>Total Carbohydrate 32g</b><span>12%</span></div>
      <div class="row in"><span>Dietary Fiber 2g</span><span>7%</span></div>
      <div class="row in"><span>Total Sugars 28g</span><span></span></div>
      <div class="row thick"><b>Protein 1g</b><span></span></div>
      <div class="row"><span>Vitamin D 0mcg</span><span>0%</span></div>
      <div class="row"><span>Calcium 20mg</span><span>2%</span></div>
      <div class="row"><span>Iron 0.7mg</span><span>4%</span></div>
      <div class="row"><span>Potassium 290mg</span><span>6%</span></div>
      <p class="foot">*The % Daily Value tells you how much a nutrient in a serving adds to a daily diet. Ingredients: salt, herbs, onion.</p>
    </div>
  </article>

</main>
</body>
</html>
```